Corvalen Capital Modern Business Card

We need a modern business card template designed for Corvalen Capital.
Corvalen Capital is a diversified global cryptocurrency investment fund.

The font under the logo: Hiragino Kaku Gothic Pro

Color Hexcode: Main colors white (ffffff) & teal (188383), we are open to adding #fcca46 as an accent

Need time to get feedback from my team and to make sure designers better understand the brief.

Target Market(s)

Accredited Investors, high net worth individuals and institutional investors

Industry/Entity Type

Investment

Contact Information for Business Card

Contact Information should contain
Name
main phone +1 720 555 0147
cell
email

Font styles to use
Sans Serif
Other font styles liked:
• Hiragino Kaku Gothic Pro

Requirements
Must have
• would like to have icons that identify the contact information
• include our website: www.corvalencapital.example
• include our Tagline: Diversified Crypto Investment Funds
Nice to have
• Would like to have a simple back side with the logo (without the words) and plenty of space

```html
<!DOCTYPE html>
<html lang="en">
<head>
<meta charset="utf-8">
<title>Corvalen Capital Business Card</title>
<link rel="stylesheet" href="https://fonts.googleapis.com/css2?family=Zen+Kaku+Gothic+New:wght@400;500;700&display=swap">
<style>
  :root {
    --backdrop: #2f4249;
    --card: #ffffff;
    --teal: #229594;
    --ink: #1b1b1b;
    --muted: #4a4a4a;
    --rule: #2a2a2a;
  }
  * { box-sizing: border-box; margin: 0; padding: 0; }
  html, body {
    width: 1200px;
    height: 900px;
    overflow: hidden;
    background: var(--backdrop);
    font-family: "Zen Kaku Gothic New", sans-serif;
    color: var(--ink);
  }
  .canvas {
    width: 1200px;
    height: 900px;
    display: flex;
    flex-direction: column;
    align-items: center;
    justify-content: center;
    gap: 30px;
  }
  .card {
    width: 700px;
    height: 400px;
    background: var(--card);
    position: relative;
  }
  /* Front side */
  .card-front .brand {
    position: absolute;
    left: 30px;
    top: 0;
    width: 270px;
    height: 400px;
    display: flex;
    flex-direction: column;
    align-items: center;
    justify-content: center;
  }
  .brand-square {
    width: 44px;
    height: 44px;
    background: var(--teal);
  }
  .brand-name {
    font-size: 22px;
    font-weight: 400;
    letter-spacing: 0.5px;
    text-transform: uppercase;
    color: var(--ink);
    white-space: nowrap;
    margin-top: 18px;
  }
  .tagline {
    font-size: 11px;
    font-weight: 500;
    letter-spacing: 0.6px;
    color: var(--muted);
    white-space: nowrap;
    margin-top: 8px;
  }
  .divider {
    position: absolute;
    left: 318px;
    top: 105px;
    width: 2px;
    height: 180px;
    background: var(--rule);
  }
  .details {
    position: absolute;
    left: 360px;
    top: 100px;
  }
  .person-name {
    font-size: 27px;
    font-weight: 700;
    line-height: 1;
  }
  .person-title {
    font-size: 13px;
    font-weight: 700;
    letter-spacing: 0.4px;
    margin-top: 8px;
  }
  .address {
    font-size: 14px;
    font-weight: 700;
    letter-spacing: 0.5px;
    line-height: 1.45;
    margin-top: 24px;
    font-style: normal;
  }
  .contact-list {
    list-style: none;
    margin-top: 14px;
  }
  .contact-item {
    display: flex;
    align-items: center;
    gap: 14px;
    font-size: 14px;
    font-weight: 700;
    letter-spacing: 0.3px;
    line-height: 21px;
    white-space: nowrap;
  }
  .contact-item.phone { font-size: 15px; letter-spacing: 1px; }
  .contact-icon { width: 18px; height: 14px; flex: none; }
  /* Back side */
  .card-back {
    display: flex;
    align-items: center;
    justify-content: center;
    gap: 20px;
  }
  .card-back .brand-square { width: 52px; height: 52px; }
  .card-back .brand-name { font-size: 38px; margin-top: 0; }
</style>
</head>
<body>
<main class="canvas">
  <section class="card card-front" aria-label="Business card front">
    <div class="brand">
      <div class="brand-square"></div>
      <div class="brand-name">Corvalen Capital</div>
      <p class="tagline">Diversified Crypto Investment Funds</p>
    </div>
    <div class="divider"></div>
    <div class="details">
      <h1 class="person-name">Daniel Reyes</h1>
      <p class="person-title">Investment Advisor</p>
      <address class="address">48 Meridian Avenue,<br>Austin TX 78701</address>
      <ul class="contact-list">
        <li class="contact-item phone">
          <svg class="contact-icon" viewBox="0 0 18 14" aria-hidden="true">
            <ellipse cx="9" cy="7" rx="9" ry="7" fill="var(--teal)"/>
            <path d="M5 6.5c0-1.5 8-1.5 8 0v.8h-2v-.8H7v.8H5z M6.5 8h5l.8 2.5H5.7z" fill="#fff"/>
          </svg>
          <span>+1 720 555 0147</span>
        </li>
        <li class="contact-item phone">
          <svg class="contact-icon" viewBox="0 0 18 14" aria-hidden="true">
            <ellipse cx="9" cy="7" rx="9" ry="7" fill="var(--teal)"/>
            <rect x="6.8" y="3" width="4.4" height="8" rx="0.8" fill="none" stroke="#fff" stroke-width="1"/>
            <circle cx="9" cy="9.4" r="0.6" fill="#fff"/>
          </svg>
          <span>+1 720 555 0193</span>
        </li>
        <li class="contact-item">
          <svg class="contact-icon" viewBox="0 0 18 14" aria-hidden="true">
            <ellipse cx="9" cy="7" rx="9" ry="7" fill="var(--teal)"/>
            <rect x="5" y="4.5" width="8" height="5.5" fill="none" stroke="#fff" stroke-width="1"/>
            <path d="M5 4.5l4 3 4-3" fill="none" stroke="#fff" stroke-width="1"/>
          </svg>
          <span>daniel.reyes@corvalencapital.example</span>
        </li>
        <li class="contact-item">
          <svg class="contact-icon" viewBox="0 0 18 14" aria-hidden="true">
            <ellipse cx="9" cy="7" rx="9" ry="7" fill="var(--teal)"/>
            <circle cx="9" cy="7" r="3.8" fill="none" stroke="#fff" stroke-width="0.9"/>
            <ellipse cx="9" cy="7" rx="1.6" ry="3.8" fill="none" stroke="#fff" stroke-width="0.9"/>
            <path d="M5.2 7h7.6" stroke="#fff" stroke-width="0.9"/>
          </svg>
          <span>www.corvalencapital.example</span>
        </li>
      </ul>
    </div>
  </section>

  <section class="card card-back" aria-label="Business card back">
    <div class="brand-square"></div>
    <div class="brand-name">Corvalen Capital</div>
  </section>
</main>
</body>
</html>
```